Logo and Double sided business card

We need a logo and business card for a Point of Sale Business, Website is www.tillcrest.com.au - this is being worked on at the moment. There is a logo on the website - but this is more of a placement /logo and needs to be redesigned.
The address for Details for the Business card are

Person Name
TILL CREST
27/3 Worrin St
Brindlemere 2158
Ph 1300 482 519 (1300 TIL 519)
Email : Person@tillcrest.com.au
Web: www.tillcrest.com.au

Our company will be a Point of Sale installation and Support business. We Specialise in the Quandel Tivra system.

We do
Installation of POS Systems
Support and Maintenance of existing POS
Tivra POS support
Updates

Target Market(s)

Restaurants, hotels, retail shops

Industry/Entity Type

Business

Contact Information for Business Card

Person Name
TILL CREST
27/3 Worrin St
Brindlemere 2158
Web: www.tillcrest.com.au

Logo Text

Till Crest

Font styles to use
Serif

Requirements
Must have
• We must have the source graphics in editable formats for both logo and business card.

```html
<!DOCTYPE html>
<html lang="en">
<head>
<meta charset="utf-8">
<title>Till Crest – Business Card</title>
<link rel="stylesheet" href="https://fonts.googleapis.com/css2?family=Crimson+Text:wght@400;600&display=swap">
<style>
  :root {
    --backdrop: #ececec;
    --card-front: #623f41;
    --card-back: #2d2215;
    --ink-light: #efe6e3;
    --ink-muted: #d9cac7;
    --brand-orange: #e6920f;
    --rule: #d8c8c6;
  }
  * { margin: 0; padding: 0; box-sizing: border-box; }
  html, body {
    width: 1200px; height: 900px; overflow: hidden;
    background: var(--backdrop);
    font-family: "Crimson Text", Georgia, serif;
  }
  .sheet {
    position: relative; width: 1200px; height: 900px;
    display: flex; align-items: center; justify-content: center; gap: 50px;
  }
  .card {
    position: relative; width: 525px; height: 300px;
    box-shadow: 0 6px 18px rgba(0,0,0,0.18);
  }
  .card--front { background: var(--card-front); color: var(--ink-light); }
  .card--back { background: var(--card-back); }

  .edge-rule {
    position: absolute; left: 28px; width: 1px; background: var(--rule);
  }
  .edge-rule--top { top: 0; height: 78px; }
  .edge-rule--bottom { bottom: 0; height: 34px; }

  .holder { position: absolute; left: 40px; top: 96px; }
  .holder__name { font-size: 21px; letter-spacing: 0.5px; line-height: 1; }
  .holder__role { font-size: 11px; color: var(--ink-muted); margin-top: 3px; }

  .contact { position: absolute; left: 24px; top: 166px; list-style: none; }
  .contact__item {
    display: flex; align-items: center; gap: 6px;
    font-size: 15px; line-height: 19px;
  }
  .contact__item--gap { margin-top: 6px; }
  .contact__icon { width: 12px; height: 12px; flex: none; }
  .contact__line { padding-left: 18px; font-size: 15px; line-height: 19px; }

  .brand {
    position: absolute; display: flex; flex-direction: column; align-items: center;
    color: var(--brand-orange);
  }
  .brand__mark {
    width: 80px; height: 80px; border-radius: 50%;
    border: 3px solid var(--brand-orange);
  }
  .brand__name {
    font-weight: 600; font-size: 36px; line-height: 1; margin-top: 10px;
    white-space: nowrap;
  }
  .card--front .brand { right: 36px; top: 120px; }
  .card--back .brand { left: 50%; top: 50%; transform: translate(-50%, -50%); }
</style>
</head>
<body>
<main class="sheet">
  <section class="card card--front" aria-label="Business card front">
    <span class="edge-rule edge-rule--top"></span>
    <span class="edge-rule edge-rule--bottom"></span>

    <div class="holder">
      <p class="holder__name">Xxxxx Xxxxxx</p>
      <p class="holder__role">Director</p>
    </div>

    <ul class="contact">
      <li class="contact__item">
        <svg class="contact__icon" viewBox="0 0 12 12" aria-hidden="true"><circle cx="6" cy="6" r="6" fill="#efe6e3"/><rect x="4" y="2.5" width="4" height="7" rx="1" fill="#623f41"/></svg>
        1300 482 519 (1300 TIL 519)
      </li>
      <li class="contact__item">
        <svg class="contact__icon" viewBox="0 0 12 12" aria-hidden="true"><circle cx="6" cy="6" r="6" fill="#efe6e3"/><rect x="2.8" y="3.8" width="6.4" height="4.4" fill="#623f41"/><path d="M2.8 3.8 6 6.4 9.2 3.8" stroke="#efe6e3" stroke-width="0.8" fill="none"/></svg>
        Person@tillcrest.com.au
      </li>
      <li class="contact__item">
        <svg class="contact__icon" viewBox="0 0 12 12" aria-hidden="true"><circle cx="6" cy="6" r="6" fill="#efe6e3"/><circle cx="6" cy="6" r="3.4" fill="none" stroke="#623f41" stroke-width="0.9"/><path d="M2.6 6h6.8M6 2.6v6.8" stroke="#623f41" stroke-width="0.8"/></svg>
        www.tillcrest.com.au
      </li>
      <li class="contact__item contact__item--gap">
        <svg class="contact__icon" viewBox="0 0 12 12" aria-hidden="true"><circle cx="6" cy="6" r="6" fill="#efe6e3"/><path d="M2.8 6.2 6 3.2l3.2 3H8.2v2.8H3.8V6.2z" fill="#623f41"/></svg>
        27/3 Worrin St
      </li>
      <li class="contact__line">Brindlemere 2158</li>
    </ul>

    <div class="brand">
      <span class="brand__mark" aria-hidden="true"></span>
      <span class="brand__name">Till Crest</span>
    </div>
  </section>

  <section class="card card--back" aria-label="Business card back">
    <div class="brand">
      <span class="brand__mark" aria-hidden="true"></span>
      <span class="brand__name">Till Crest</span>
    </div>
  </section>
</main>
</body>
</html>
```